Medical service promotional magnet representing our 7 day service.

Please design a magnet in the number 7 to represent a 7 day service. The size needs to be no more than 80mmx90mm be bright and show the service has 2 businesses that cover the 7 days. The logos are added to assist. Perhaps 2 puzzle pieces or something similar would be good.
We have
Norvale Clinic Link Nightcare
Open Monday to Friday 6-10pm
Saturday 1pm - 10pm
Sunday and public holidays 9am -10pm.
Phone 74119352

Also have the locum service

Norvale Ring For Care
Open Monday to Thursday 6pm - 8am
Friday 6pm to Monday 8am
Public holidays 24 hours.
Phone 741196083

Hi Designers,
Could you design a magnet in the shape of a number 7 please. If you can include the logos that would be great. The 7 represents the 7 days a week - perhaps the 7 could be made of 2 puzzle pieces making the number 7 including both logos and colours. We look forward to seeing your designs.
Cheers Bea and Team.

```html
<!DOCTYPE html>
<html lang="en">
<head>
<meta charset="utf-8">
<title>Norvale 7 Day Service Magnet</title>
<link rel="stylesheet" href="https://fonts.googleapis.com/css2?family=Jost:wght@400;700&display=swap">
<style>
  :root {
    --page: #ffffff;
    --frame: #231f20;
    --clinic-red: #e32b2b;
    --care-blue: #1b96d1;
    --seven: #ffffff;
    --heading: #ffffff;
    --clinic-copy: #f6d3d0;
    --care-copy: #d8eef9;
  }
  html, body {
    margin: 0;
    padding: 0;
    width: 1200px;
    height: 1000px;
    overflow: hidden;
    background: var(--page);
    font-family: "Jost", "Futura", sans-serif;
  }
  .canvas {
    position: relative;
    width: 1200px;
    height: 1000px;
  }
  .magnet-frame {
    position: absolute;
    left: 326px;
    top: 171px;
    width: 526px;
    height: 591px;
    border: 18px solid var(--frame);
    border-top-width: 19px;
    border-bottom-width: 22px;
    background: var(--page);
  }
  .panel {
    position: absolute;
    top: 220px;
    height: 532px;
  }
  .panel--clinic { left: 366px; width: 245px; background: var(--clinic-red); }
  .panel--care { left: 611px; width: 235px; background: var(--care-blue); }
  .seven {
    position: absolute;
    left: 0;
    top: 0;
    width: 1200px;
    height: 1000px;
  }
  .txt {
    position: absolute;
    margin: 0;
    white-space: nowrap;
  }
  .service-name {
    font-weight: 700;
    font-size: 27px;
    line-height: 35px;
    color: var(--heading);
    letter-spacing: 0.3px;
  }
  .service-name--care {
    font-size: 25px;
    line-height: 35px;
    letter-spacing: 0.2px;
    text-align: right;
  }
  .hours {
    font-weight: 400;
    font-size: 22px;
    line-height: 30px;
    letter-spacing: 0.4px;
  }
  .hours--clinic { color: var(--clinic-copy); }
  .hours--care { color: var(--care-copy); text-align: right; }
  .phone {
    font-weight: 700;
    font-size: 24px;
    line-height: 28px;
    color: var(--heading);
    letter-spacing: 0.3px;
  }
  .day-tag {
    font-weight: 700;
    font-size: 21px;
    line-height: 27px;
    color: var(--heading);
  }
</style>
</head>
<body>
<div class="canvas">
  <div class="magnet-frame"></div>
  <div class="panel panel--clinic"></div>
  <div class="panel panel--care"></div>

  <svg class="seven" viewBox="0 0 1200 1000" aria-hidden="true">
    <polygon fill="var(--seven)" points="465,264 731,264 731,288 563,632 484,632 632,327 465,327"/>
  </svg>

  <h2 class="txt service-name" style="left:378px; top:329px;">Norvale<br>Clinic Link<br>Nightcare</h2>
  <p class="txt hours hours--clinic" style="left:376px; top:444px;">Mon to Fri<br>6-10pm</p>
  <p class="txt hours hours--clinic" style="left:376px; top:520px;">Sat<br>1-10pm</p>
  <p class="txt hours hours--clinic" style="left:376px; top:600px;">Sunday<br>&amp; public holidays<br>9am -10pm</p>
  <p class="txt phone" style="left:377px; top:718px;">Phone 74119352</p>

  <h2 class="txt service-name service-name--care" style="right:362px; top:372px;">Norvale<br>Ring For Care</h2>
  <p class="txt hours hours--care" style="right:359px; top:453px;">Mon to Thurs<br>6pm-8am</p>
  <p class="txt hours hours--care" style="right:359px; top:523px;">Friday 6pm<br>to&nbsp;&nbsp;<br>Monday 8am</p>
  <p class="txt hours hours--care" style="right:356px; top:640px;">Public holidays<br>24 hours.</p>
  <p class="txt phone" style="left:617px; top:717px;">Phone 741196083</p>

  <p class="txt day-tag" style="left:614px; top:568px;">Day</p>
  <p class="txt day-tag" style="left:581px; top:596px;">Service</p>
</div>
</body>
</html>
```